Ostrel Appraisals BV business cards (a financial services company)

I am looking for a business card design that stands out in the financial advisory field of business & intellectual property valuation. The business card design should be conservative, yet different. Address details have changed since the attached business card. New address is:

Molenvlietkade 27
4817 KT Leiden
The Netherlands

Telephone number remains the same.

```html
<!DOCTYPE html>
<html lang="en">
<head>
<meta charset="utf-8">
<title>Ostrel Appraisals BV – Business Cards</title>
<link href="https://fonts.googleapis.com/css2?family=Roboto:wght@400;500;700&display=swap" rel="stylesheet">
<style>
  :root {
    --page-bg: #d8d5d1;
    --card-top: #2a2a2a;
    --card-bottom: #0b0b0b;
    --ink-strong: #8a8a8a;
    --ink-soft: #7c7c7c;
    --ink-mark: #8e8e8e;
  }
  * { margin: 0; padding: 0; box-sizing: border-box; }
  html, body {
    width: 1200px; height: 1200px; overflow: hidden;
    background: var(--page-bg);
    font-family: "Roboto", sans-serif;
  }
  .sheet { position: relative; width: 1200px; height: 1200px; }
  .card {
    position: absolute; left: 196px; width: 810px; height: 462px;
    border-radius: 30px;
    background: radial-gradient(ellipse at 50% 20%, var(--card-top) 0%, #151515 55%, var(--card-bottom) 100%);
    box-shadow: 0 6px 18px rgba(0,0,0,.35);
    color: var(--ink-soft);
    text-align: center;
  }
  .card--front { top: 96px; }
  .card--back { top: 602px; }

  .brand {
    position: absolute; left: 0; right: 0;
    display: flex; align-items: center; justify-content: center; gap: 18px;
    color: var(--ink-mark); font-weight: 500; letter-spacing: 3px;
    text-transform: uppercase;
  }
  .brand__square { background: var(--ink-mark); flex: none; }
  .card--front .brand { top: 190px; font-size: 44px; }
  .card--front .brand__square { width: 34px; height: 34px; }
  .card--back .brand { top: 110px; font-size: 32px; }
  .card--back .brand__square { width: 24px; height: 24px; }

  .person { position: absolute; top: 258px; left: 0; right: 0; }
  .person__name { font-size: 24px; font-weight: 700; color: var(--ink-strong); }
  .person__creds { font-size: 19px; font-weight: 500; }
  .person__role { font-size: 19px; margin-top: 2px; }
  .divider {
    position: absolute; top: 344px; left: 50%; width: 54px; margin-left: -27px;
    border-top: 2px solid #555;
  }
  .contact { position: absolute; top: 388px; left: 0; right: 0; font-size: 17px; }
  .contact__line { display: flex; justify-content: center; align-items: center; gap: 5px; }
  .contact__icon { width: 15px; height: 15px; fill: none; stroke: var(--ink-soft); stroke-width: 1.4; }
  .contact__address { margin-top: 12px; }
</style>
</head>
<body>
<main class="sheet">
  <section class="card card--front">
    <div class="brand"><span class="brand__square"></span>Ostrel Appraisals</div>
  </section>

  <section class="card card--back">
    <div class="brand"><span class="brand__square"></span>Ostrel Appraisals</div>

    <div class="person">
      <p><span class="person__name">MAARTEN VOS</span> <span class="person__creds">CFA, ASA, RV</span></p>
      <p class="person__role">Managing Director</p>
    </div>

    <div class="divider"></div>

    <div class="contact">
      <p class="contact__line">
        <svg class="contact__icon" viewBox="0 0 16 16"><path d="M4 1.5l2.5 3-1.5 1.8a9 9 0 0 0 4.7 4.7l1.8-1.5 3 2.5-1.8 2.2C7 14 2 9 1.8 3.3z"/></svg>
        +31 (0)70 555 0142 |
        <svg class="contact__icon" viewBox="0 0 16 16"><rect x="1.5" y="3.5" width="13" height="9"/><path d="M1.5 3.5l6.5 5 6.5-5"/></svg>
        mvos@ostrelappraisals.com |
        <svg class="contact__icon" viewBox="0 0 16 16"><circle cx="8" cy="8" r="6.5"/><ellipse cx="8" cy="8" rx="3" ry="6.5"/><path d="M1.5 8h13M2.5 5h11M2.5 11h11"/></svg>
        www.ostrelappraisals.com
      </p>
      <p class="contact__address">Molenvlietkade 27 4817 KT Leiden The Netherlands</p>
    </div>
  </section>
</main>
</body>
</html>
```